Refer a Friend A5 Flyer for Healthcare Staff

We need an A5 flyer that we can hand out to existing and new staff members promoting our Refer a friend Scheme. We need the leaflet to encourage staff to talk to their family and friends about joining our Healthcare Agency, which provides staff to local care related establishments. Using our logo and brand colours blue and green, as per our website, the final design will need to clearly convey the benefits and attractions of referring additional staff to the team. In addition is the promotion of our Chatterbox page, requesting staff to like the page and to like and share various posts.

Target Market(s)

Healthcare and potential Healthcare Staff

Industry/Entity Type

Healthcare

Colors
33b8a4
3277b5

Requirements
Must have
• Company Logo, Brand colours,
• text; "Refer a Friend and receive a £50 Bonus after just 1 completed shift"
• text; "3 easy steps to refer a friend, 1 Fill out your name on the back of your Business Card 2 Hand the card to your friend or any person you wish to refer, 3 ask your friend to present the card to us when they attend their interview"
• text; "Like and share any of our Open Days on Chatterbox for a chance to win a prize, you can find us easily by searching @CarewellPlacementGroup"
• text; "Like our Page to stay up to date with our events and offers"
Nice to have
• care worker / elderly care / support worker pictures
• Content / pics from website www.carewellplacementgroup.co.uk

```html
<!DOCTYPE html>
<html lang="en">
<head>
<meta charset="utf-8">
<title>Carewell Placement – Refer a Friend Flyer</title>
<link rel="stylesheet" href="https://fonts.googleapis.com/css2?family=Roboto:wght@400;500;700;900&display=swap">
<style>
  :root {
    --brand-blue: #0a41a1;
    --brand-green: #00a383;
    --ink-grey: #3c3c3c;
    --backdrop: #eceef2;
    --paper: #ffffff;
  }
  * { box-sizing: border-box; margin: 0; padding: 0; }
  html, body { width: 1040px; height: 1200px; overflow: hidden; background: var(--backdrop); }
  body { position: relative; font-family: "Roboto", Arial, sans-serif; }

  .flyer {
    position: absolute; left: 104px; top: 0;
    width: 957px; height: 1380px;
    transform: scale(0.8696); transform-origin: 0 0;
    background: var(--paper); overflow: hidden;
  }
  .abs { position: absolute; }

  /* brand */
  .brand { left: 0; width: 957px; top: 92px; display: flex; justify-content: center; align-items: center; gap: 18px; }
  .brand-dot { width: 34px; height: 34px; border-radius: 50%; background: var(--brand-blue); }
  .brand-name { font-size: 54px; font-weight: 400; color: var(--brand-blue); letter-spacing: 0.5px; }
  .brand-line { left: 0; width: 957px; top: 168px; text-align: center; font-size: 18px; color: var(--ink-grey); }

  /* hero */
  .hero-photo { left: 0; top: 239px; width: 957px; height: 440px;
    background: linear-gradient(90deg, #f6efe6 0%, #efe2d3 38%, #e8d6c6 55%, #3b78c9 80%, #2a63b3 100%); }
  .hero-copy { left: 10px; top: 292px; width: 330px; text-align: center; color: var(--brand-blue); }
  .hero-copy .lead { font-size: 33px; line-height: 45px; }
  .hero-copy .amount { font-size: 72px; font-weight: 900; line-height: 90px; }
  .hero-copy .tail { font-size: 33px; line-height: 44px; }

  .bands { left: 0; top: 580px; width: 957px; height: 190px; }

  /* steps */
  .steps-title { left: 563px; top: 728px; width: 330px; text-align: center; font-size: 24px; font-weight: 500; color: #111;
    padding-bottom: 8px; border-bottom: 2px solid var(--brand-green); }
  .steps-art { left: 0; top: 780px; width: 957px; height: 220px; }
  .step-caption { top: 1010px; width: 280px; text-align: center; font-size: 18px; line-height: 23px; color: var(--ink-grey); }

  /* social */
  .social-badge { left: 45px; top: 1070px; width: 200px; height: 175px; border-radius: 14px;
    background: linear-gradient(160deg, #2f6fd1 0%, var(--brand-blue) 100%); }
  .social-copy { left: 235px; top: 1120px; width: 660px; text-align: center; font-size: 27px; line-height: 32px; color: var(--brand-blue); }
  .social-copy strong { color: var(--brand-green); font-weight: 700; }
  .handle { left: 235px; top: 1195px; width: 660px; display: flex; justify-content: center; align-items: center; gap: 14px;
    font-size: 27px; color: var(--brand-green); }
  .handle-dot { width: 34px; height: 34px; border-radius: 50%; background: var(--brand-blue); }

  .footer { left: 0; top: 1245px; width: 957px; height: 135px; background: var(--brand-blue);
    color: #fff; text-align: center; font-size: 31px; line-height: 38px; letter-spacing: 2.5px; padding-top: 16px; }
</style>
</head>
<body>
<main class="flyer">
  <div class="abs brand"><span class="brand-dot"></span><span class="brand-name">Carewell Placement</span></div>
  <div class="abs brand-line">Keeping it Simple</div>

  <div class="abs hero-photo" role="img" aria-label="Photo of a smiling care worker in blue scrubs beside an elderly woman"></div>
  <div class="abs hero-copy">
    <p class="lead">Refer a Friend and<br>receive a</p>
    <p class="amount">£50</p>
    <p class="tail">bonus after just<br>1 completed shift</p>
  </div>

  <svg class="abs bands" viewBox="0 0 957 190" aria-hidden="true">
    <polygon points="0,5 957,75 957,190 0,190" fill="var(--brand-blue)"/>
    <polygon points="0,92 957,92 957,105 0,175" fill="var(--brand-green)"/>
    <polygon points="0,175 957,105 957,190 0,190" fill="#fff"/>
  </svg>

  <h2 class="abs steps-title">3 Easy steps to refer a friend</h2>

  <svg class="abs steps-art" viewBox="0 780 957 220" aria-hidden="true">
    <g fill="none" stroke="var(--brand-green)" stroke-width="4">
      <path d="M0,870 Q30,855 65,845"/>
      <path d="M262,843 Q310,850 355,872"/>
      <path d="M550,945 Q610,952 665,945"/>
      <path d="M862,890 Q920,860 957,815"/>
    </g>
    <circle cx="163" cy="890" r="105" fill="#fff" stroke="var(--brand-green)" stroke-width="3" stroke-dasharray="3 6"/>
    <circle cx="458" cy="893" r="105" fill="#fff" stroke="var(--brand-blue)" stroke-width="3" stroke-dasharray="3 6"/>
    <circle cx="763" cy="893" r="105" fill="#fff" stroke="var(--brand-green)" stroke-width="3" stroke-dasharray="3 6"/>

    <g fill="#fff" stroke-width="2" font-family="Roboto, Arial, sans-serif" font-size="19" text-anchor="middle">
      <circle cx="255" cy="805" r="15" stroke="var(--brand-green)"/>
      <text x="255" y="812" fill="#111" stroke="none">1</text>
      <circle cx="558" cy="972" r="15" stroke="var(--brand-blue)"/>
      <text x="558" y="979" fill="#111" stroke="none">2</text>
      <circle cx="873" cy="822" r="15" stroke="var(--brand-green)"/>
      <text x="873" y="829" fill="#111" stroke="none">3</text>
    </g>

    <!-- card icon -->
    <g fill="none" stroke="var(--brand-green)" stroke-width="5" stroke-linejoin="round">
      <rect x="105" y="850" width="124" height="82" rx="8"/>
      <path d="M118,846 L125,830 L215,838 L220,850"/>
      <circle cx="148" cy="880" r="12"/>
      <path d="M126,915 Q148,890 170,915"/>
      <path d="M184,875 h30 M184,891 h30 M184,907 h30"/>
    </g>
    <!-- hand-over card icon -->
    <g fill="none" stroke="var(--brand-blue)" stroke-width="5" stroke-linejoin="round">
      <rect x="391" y="880" width="88" height="52" rx="6"/>
      <path d="M425,880 L440,840 L468,852 L500,835 L535,860 L482,912"/>
      <path d="M500,835 L512,825 L535,845 L525,858 Z" fill="var(--brand-blue)"/>
    </g>
    <!-- interview table icon -->
    <g fill="none" stroke="var(--brand-green)" stroke-width="4">
      <path d="M720,895 h86 M735,895 v40 M791,895 v40"/>
      <path d="M700,905 v30 M700,935 h14 M826,905 v30 M826,935 h-14"/>
      <rect x="728" y="845" width="28" height="20" rx="3" fill="var(--brand-green)"/>
      <rect x="770" y="850" width="22" height="16" rx="2" stroke="var(--brand-blue)" stroke-width="2"/>
    </g>
  </svg>

  <p class="abs step-caption" style="left:12px">Fill out your name on the back of your Business Card</p>
  <p class="abs step-caption" style="left:288px">Hand the card to your friend or any person you wish to refer</p>
  <p class="abs step-caption" style="left:588px;width:340px">Ask your friend to present the card to us when they attend their interview</p>

  <div class="abs social-badge" role="img" aria-label="Thumbs-up graphic with Like and Share lettering"></div>
  <p class="abs social-copy">any of our <strong>Open Days</strong> on Chatterbox for a chance to win a prize, you can find us easily by searching</p>
  <p class="abs handle"><span class="handle-dot"></span><span>@CarewellPlacementGroup</span></p>

  <footer class="abs footer">Like our Page to stay up to date with our<br>events and offers.</footer>
</main>
</body>
</html>
```